Elegant, High End Integrated Wellness Healthcare Practice

We need a brochure designed for an integrated mind-body wellness healthcare practice (www.larchveilclinic.com) . This brochure will be used when we cold call prospects (physicians to refer to our office, and potential consumers to utilize our services). Our practice is geographically located in the middle Tennessee USA region, although we have plans to become an international company as many of our offerings can be accessed anywhere in the world. Ultimately our goal is to have this brochure used as a leave-behind in an effort to introduce our integrated offerings to increase market share. The final product brochure should be both elegant and serious, with clean lines but also convey warmth and trust, as individuals who are coming for our services have usually struggled with their health for a significant amount of time before finding our practice.

The design brief was very specific about providing a high-end science-based 2-page brochure (not flier). Several designs submitted were fliers. The other designs were heavy on yoga or "woo woo" non-science-based looking pictures. This is a flier to appeal to physicians and other healthcare providers. Therefore the design must speak science and evidence-based methods of mind and body wellness care. I would also like to appeal to the other designers I paid extra for their submissions and who have indicated they will "respond in the coming days."

```html
<!DOCTYPE html>
<html lang="en">
<head>
<meta charset="utf-8">
<title>Larchveil Clinic – Brochure</title>
<link rel="stylesheet" href="https://fonts.googleapis.com/css2?family=Montserrat:wght@700&family=Jost:wght@400;500&family=Maven+Pro:wght@400;500&display=swap">
<style>
  :root {
    --navy: #0f2150;
    --green: #6aa834;
    --ring: #9fb47f;
    --paper: #ffffff;
    --stage: #333333;
    --ink: #1d2433;
    --muted: #555b66;
  }
  * { margin: 0; padding: 0; box-sizing: border-box; }
  html, body { width: 805px; height: 1200px; overflow: hidden; background: var(--stage); }
  .spread { position: absolute; left: 63px; width: 678px; height: 527px; background: var(--paper); overflow: hidden; }
  .spread--outer { top: 56px; }
  .spread--inner { top: 618px; height: 526px; }
  .spread > svg.backdrop { position: absolute; inset: 0; }
  .abs { position: absolute; }

  .hero-title { font-family: 'Jost', sans-serif; font-weight: 500; color: var(--green); font-size: 18px; line-height: 20px; left: 32px; top: 230px; white-space: nowrap; }
  .hero-sub { font-family: 'Jost', sans-serif; color: #fff; font-size: 11.4px; line-height: 15.5px; left: 32px; top: 274px; white-space: nowrap; }

  .section-title { font-family: 'Montserrat', sans-serif; font-weight: 700; color: var(--navy); font-size: 16.5px; line-height: 20px; }
  .accent-bar { height: 3px; background: var(--green); border-radius: 2px; }

  .contact-intro { font-family: 'Maven Pro', sans-serif; color: var(--muted); font-size: 7.4px; line-height: 10px; left: 35px; top: 454px; width: 118px; }
  .social { left: 36px; top: 498px; display: flex; gap: 3.5px; }
  .social span { width: 9.5px; height: 9.5px; border: 1.2px solid var(--green); border-radius: 50%; }
  .contact-list { font-family: 'Maven Pro', sans-serif; color: var(--ink); font-size: 7.4px; line-height: 10.3px; left: 178px; top: 453px; list-style: none; }
  .contact-list li { display: flex; align-items: flex-start; gap: 2px; }
  .contact-list svg { width: 6px; height: 6px; margin-top: 2px; flex: none; }

  .brand { left: 370px; top: 377px; display: flex; align-items: center; gap: 10px; }
  .brand-dot { width: 50px; height: 50px; border-radius: 50%; border: 3px solid var(--green); flex: none; }
  .brand-name { font-family: 'Montserrat', sans-serif; font-weight: 700; color: var(--navy); font-size: 17px; line-height: 26px; letter-spacing: 0.6px; }
  .tagline { font-family: 'Maven Pro', sans-serif; color: var(--ink); font-size: 8.4px; line-height: 10.3px; left: 377px; top: 460px; width: 180px; }

  .body-copy { font-family: 'Jost', sans-serif; font-size: 7.6px; line-height: 10.6px; text-align: justify; width: 282px; }
  .about-copy { left: 32px; top: 72px; color: var(--ink); }
  .photo-card { top: 165px; width: 127px; height: 90px; border-radius: 8px; }
  .photo-caption { font-family: 'Maven Pro', sans-serif; color: var(--muted); font-size: 7.4px; line-height: 10px; top: 263px; width: 130px; }

  .service { position: absolute; display: flex; gap: 7px; width: 140px; }
  .service-icon { width: 31px; height: 31px; border-radius: 50%; background: var(--navy); flex: none; display: flex; align-items: center; justify-content: center; }
  .service-icon span { width: 10px; height: 10px; border-radius: 50%; border: 2px solid #fff; }
  .service h3 { font-family: 'Maven Pro', sans-serif; font-weight: 500; color: var(--ink); font-size: 8.6px; line-height: 9.5px; white-space: nowrap; }
  .service p { font-family: 'Jost', sans-serif; color: var(--muted); font-size: 5.4px; line-height: 8.2px; width: 76px; }

  .why-title { font-family: 'Montserrat', sans-serif; font-weight: 700; font-size: 17px; line-height: 20px; left: 32px; top: 395px; color: #fff; }
  .why-title em { font-style: normal; color: var(--green); }
  .why-copy { left: 32px; top: 438px; color: #fff; }
</style>
</head>
<body>

<!-- Outer spread: back panel and cover -->
<section class="spread spread--outer">
  <svg class="backdrop" width="678" height="527" viewBox="0 0 678 527">
    <defs>
      <linearGradient id="brainTone" x1="0" y1="0" x2="1" y2="1">
        <stop offset="0" stop-color="#2b4a78"/><stop offset="0.5" stop-color="#8fb4d8"/><stop offset="1" stop-color="#1b2f55"/>
      </linearGradient>
      <linearGradient id="mealTone" x1="0" y1="0" x2="1" y2="1">
        <stop offset="0" stop-color="#e4d8c4"/><stop offset="0.45" stop-color="#b58a6a"/><stop offset="0.75" stop-color="#8a4450"/><stop offset="1" stop-color="#4fc3d6"/>
      </linearGradient>
    </defs>
    <rect width="678" height="527" fill="var(--navy)"/>
    <path d="M0,362 C60,392 130,385 190,345 C235,318 270,300 310,292 C360,282 410,295 450,330 L678,320 V527 H0 Z" fill="var(--paper)"/>
    <circle cx="368" cy="200" r="122" fill="none" stroke="var(--ring)" stroke-width="34" opacity="0.3"/>
    <path d="M0,340 C60,368 130,365 190,345 C130,385 60,392 0,362 Z" fill="var(--green)"/>
    <path d="M295,296 C340,272 400,272 455,310 L450,330 C410,295 360,282 310,292 Z" fill="var(--green)"/>
    <line x1="339" y1="0" x2="339" y2="527" stroke="#e8ecf2" stroke-width="0.6" opacity="0.5"/>
    <circle cx="90" cy="45" r="150" fill="url(#brainTone)" role="img" aria-label="Hand touching a tablet with a glowing network brain above it"/>
    <path d="M214,0 C262,40 262,130 163,188 C238,128 240,50 200,0 Z" fill="var(--green)"/>
    <path d="M545,0 H678 V286 A131,131 0 1 1 440,181 Z" fill="var(--paper)"/>
    <path d="M560,0 H678 V247 L676,247 A123,123 0 1 1 448,183 Z" fill="url(#mealTone)" role="img" aria-label="Woman in sportswear eating a fresh salad bowl"/>
    <path d="M678,314 A142,142 0 0 1 606,379" fill="none" stroke="var(--green)" stroke-width="9"/>
  </svg>

  <h1 class="abs hero-title">Discover A Better<br>Way To A Better You.</h1>
  <p class="abs hero-sub">We take a completely different<br>approach to mind and body wellness!</p>

  <h2 class="abs section-title" style="left:35px; top:420px;">Contact Us</h2>
  <div class="abs accent-bar" style="left:35px; top:444px; width:38px;"></div>
  <p class="abs contact-intro">Lorem ipsum dolor sit amet, consi adipisicing elit, sed do eiustempor incididunt labore et dolore ealiqua enim ad minim veniam.</p>
  <div class="abs social"><span></span><span></span><span></span><span></span><span></span><span></span><span></span></div>

  <div class="abs accent-bar" style="left:178px; top:444px; width:42px;"></div>
  <ul class="abs contact-list">
    <li><svg viewBox="0 0 10 10"><path d="M2 1 L4 1 L5 3.5 L3.8 4.5 C4.5 6 5 6.5 6.5 7.2 L7.5 6 L10 7 L10 9 C5 10 0 5 1 1 Z" fill="var(--green)"/></svg>+1 615-555-0148</li>
    <li><svg viewBox="0 0 10 10"><rect x="0.5" y="2" width="9" height="6.5" fill="var(--green)"/><path d="M0.5 2 L5 6 L9.5 2" stroke="#fff" fill="none"/></svg>hello@larchveilclinic.com</li>
    <li><svg viewBox="0 0 10 10"><circle cx="5" cy="5" r="4.3" fill="none" stroke="var(--green)" stroke-width="1.2"/><path d="M0.7 5 H9.3 M5 0.7 V9.3" stroke="var(--green)"/></svg>www.larchveilclinic.com</li>
    <li><svg viewBox="0 0 10 10"><path d="M5 0.5 C2.5 0.5 1.5 2.3 1.5 3.8 C1.5 6 5 9.5 5 9.5 C5 9.5 8.5 6 8.5 3.8 C8.5 2.3 7.5 0.5 5 0.5 Z" fill="var(--green)"/><circle cx="5" cy="3.8" r="1.3" fill="#fff"/></svg>418 Quarry Bend Road, Fernhollow,<br>TN, United States</li>
  </ul>

  <div class="abs brand">
    <span class="brand-dot"></span>
    <span class="brand-name">LARCHVEIL<br>CLINIC</span>
  </div>
  <div class="abs accent-bar" style="left:377px; top:449px; width:38px;"></div>
  <p class="abs tagline">We help you achieve greater happiness and overcome challenges through classes, programs, and sessions.</p>
</section>

<!-- Inner spread: about, services, why us -->
<section class="spread spread--inner">
  <svg class="backdrop" width="678" height="526" viewBox="0 0 678 526">
    <defs>
      <linearGradient id="duoTone" x1="0" y1="0" x2="1" y2="1">
        <stop offset="0" stop-color="#4f6f86"/><stop offset="0.5" stop-color="#9fb5c6"/><stop offset="1" stop-color="#1f3558"/>
      </linearGradient>
    </defs>
    <path d="M0,358 C80,328 160,322 240,352 C300,375 340,402 395,402 C420,402 440,396 460,390 L678,385 V526 H0 Z" fill="var(--navy)"/>
    <path d="M0,335 C60,305 130,300 180,318 C205,327 225,338 240,352 C160,322 80,328 0,358 Z" fill="var(--green)"/>
    <path d="M280,360 C320,386 355,400 395,398 C420,398 440,392 465,386" fill="none" stroke="var(--green)" stroke-width="7"/>
    <path d="M440,359 A162,162 0 0 1 678,390" fill="none" stroke="var(--green)" stroke-width="13"/>
    <circle cx="545" cy="482" r="149" fill="url(#duoTone)" role="img" aria-label="Two people in thought with a DNA helix and heartbeat line overlay"/>
  </svg>

  <h2 class="abs section-title" style="left:32px; top:30px;">About<br>Our Company</h2>
  <p class="abs body-copy about-copy">At Larchveil Clinic, we facilitate body and mind health and wellness through an integrated functional approach to care. This method of personalized care appreciates you as a unique individual with distinct health circumstances. We tailor our body and mind approaches to address your specific health concerns. Through the combination of body and mind interventions, we address concerns such as Attention Deficit, Distractibility and learning concerns, chronic pain and inflammation conditions, and mind health conditions such as anxiety, depression, panic, and many more.</p>

  <div class="abs photo-card" style="left:32px; background:linear-gradient(180deg,#d9a08a,#f2b888 55%,#5a3a3a);" role="img" aria-label="Person in a yoga pose silhouetted against a sunset"></div>
  <div class="abs photo-card" style="left:185px; background:linear-gradient(135deg,#c84a2e,#e9efe8 45%,#8cb84a 80%,#e6b640);" role="img" aria-label="Prescription pad and stethoscope surrounded by fresh fruit and vegetables"></div>
  <p class="abs photo-caption" style="left:32px;">Lorem ipsum dolor sit conseetecreing elit, sed do eetempor incididuilaboreyr et maaliqua.</p>
  <p class="abs photo-caption" style="left:185px;">Lorem ipsum dolor sit conseetecreing elit, sed do eetempor incididuilaboreyr et maaliqua.</p>

  <h2 class="abs section-title" style="left:370px; top:30px;">Our<br>Services</h2>

  <div class="service" style="left:366px; top:82px;"><div class="service-icon"><span></span></div><div><h3>Anxiety<br>Counseling</h3><p>Lorem ipsum dolor consecritur adipisicing elit, sed do erumod tempor incididunt.</p></div></div>
  <div class="service" style="left:509px; top:82px;"><div class="service-icon"><span></span></div><div><h3>Dating &amp; Relationship<br>Counseling</h3><p>Lorem ipsum dolor consecritur adipisicing elit, sed do erumod tempor incididunt.</p></div></div>
  <div class="service" style="left:366px; top:135px;"><div class="service-icon"><span></span></div><div><h3>Family Counseling</h3><p>Lorem ipsum dolor consecritur adipisicing elit, sed do erumod tempor incididunt.</p></div></div>
  <div class="service" style="left:509px; top:135px;"><div class="service-icon"><span></span></div><div><h3>Marriage Counseling</h3><p>Lorem ipsum dolor consecritur adipisicing elit, sed do erumod tempor incididunt.</p></div></div>
  <div class="service" style="left:366px; top:184px;"><div class="service-icon"><span></span></div><div><h3>Attention Deficit<br>Disorder Treatment</h3><p>Lorem ipsum dolor consecritur adipisicing elit, sed do erumod tempor incididunt.</p></div></div>
  <div class="service" style="left:509px; top:184px;"><div class="service-icon"><span></span></div><div><h3>Self-esteem<br>Therapy</h3><p>Lorem ipsum dolor consecritur adipisicing elit, sed do erumod tempor incididunt.</p></div></div>
  <div class="service" style="left:366px; top:238px;"><div class="service-icon"><span></span></div><div><h3>Depression Counseling</h3><p>Lorem ipsum dolor consecritur adipisicing elit, sed do erumod tempor incididunt.</p></div></div>
  <div class="service" style="left:509px; top:238px;"><div class="service-icon"><span></span></div><div><h3>Grief Counseling</h3><p>Lorem ipsum dolor consecritur adipisicing elit, sed do erumod tempor incididunt.</p></div></div>

  <h2 class="abs why-title">Why<br><em>Choose Us?</em></h2>
  <p class="abs body-copy why-copy">At Larchveil Clinic, our goal is to help you achieve your vision of who you want to be and find greater personal satisfaction in life. We look forward to meeting you, discussing your challenges and opportunities, and getting started on this journey together!</p>
</section>

</body>
</html>
```